I need a Billboard Design for our company called kelMARINDO.
I'm completely open for any design idea, but it must be professional and adventurous. The Billboard is 10ft high and 20ft wide.
Our Slogan is: "The ULTIMATE HELICOPTER DOORS-OFF Experience."
"Say YES to New Adventures"
Locations: SARASOTA | TAMPA | NAPLES
Prices Starting at $99.
Hotline: (844) KEL-MARI(ndo) (844) 535-6274
www.kelMARINDO.com
Target Market(s)
Aviation, Tourism
Industry/Entity Type
Tourism
Requirements
Must have
- The Design should match our website design at www.kelMARINDO.com
Please checkout the website for ideas. Thank you

```html
<!DOCTYPE html>
<html lang="en">
<head>
<meta charset="utf-8">
<title>kelMARINDO Billboard</title>
<link href="https://fonts.googleapis.com/css2?family=Arimo:wght@400;700&family=Roboto+Condensed:wght@500;700&display=swap" rel="stylesheet">
<style>
  :root {
    --page-bg: #e9eef3;
    --board-white: #f8f9fa;
    --brand-blue: #1d36a3;
    --headline-blue: #2438a0;
    --ink: #141414;
    --white: #ffffff;
    --haze-light: #eef3f4;
    --haze-teal: #b9d0d3;
    --cabin-light: #d8cbbd;
    --cabin-dark: #8b7a6c;
  }
  * { margin: 0; padding: 0; box-sizing: border-box; }
  html, body {
    width: 1200px; height: 872px; overflow: hidden;
    background: var(--page-bg);
    font-family: "Arimo", Arial, sans-serif;
  }
  .billboard {
    position: absolute; left: 40px; top: 184px;
    width: 1120px; height: 504px;
    background: var(--board-white);
    overflow: hidden;
  }
  .billboard-art { position: absolute; inset: 0; }
  .brand {
    position: absolute; left: 44px; top: 66px;
    display: flex; align-items: center; gap: 8px;
    font-size: 26px; font-weight: 400; color: var(--brand-blue);
    letter-spacing: 0.5px;
  }
  .brand-dot {
    width: 16px; height: 16px; border-radius: 50%;
    background: var(--brand-blue);
  }
  .slogan {
    position: absolute; left: 308px; top: 56px;
    color: var(--headline-blue);
  }
  .slogan-top { font-size: 30px; letter-spacing: 0.6px; line-height: 1; }
  .slogan-bottom {
    display: flex; align-items: baseline; gap: 10px;
    margin-top: 14px; padding-left: 8px;
  }
  .slogan-doors { font-size: 21px; letter-spacing: 0.4px; }
  .slogan-experience { font-size: 43px; font-weight: 700; color: var(--ink); }
  .tagline {
    position: absolute; left: 62px; top: 186px;
    font-size: 36px; color: var(--headline-blue); letter-spacing: 0.4px;
    white-space: nowrap; word-spacing: 4px;
  }
  .tagline strong { font-weight: 700; }
  .price-badge {
    position: absolute; left: 78px; top: 252px;
    width: 192px; height: 178px; border-radius: 50%;
    background: var(--brand-blue); border: 4px solid var(--white);
    color: var(--white); text-align: center;
    font-family: "Roboto Condensed", "Arial Narrow", sans-serif;
    display: flex; flex-direction: column; justify-content: center;
  }
  .price-label { font-size: 23px; font-weight: 500; line-height: 1.3; }
  .price-amount { font-size: 48px; font-weight: 700; line-height: 1.05; }
  .hotline {
    position: absolute; left: 295px; top: 390px;
    color: var(--white); font-weight: 700; white-space: nowrap;
    display: flex; align-items: baseline; gap: 8px;
  }
  .hotline-label { font-size: 19px; }
  .hotline-number { font-size: 27px; letter-spacing: 0.5px; }
  .locations {
    position: absolute; left: 80px; top: 462px;
    color: var(--white); font-size: 19px; font-weight: 700; letter-spacing: 0.5px;
  }
  .website {
    position: absolute; left: 815px; top: 466px;
    color: var(--white); font-size: 20px; font-weight: 700;
  }
</style>
</head>
<body>
  <div class="billboard">
    <svg class="billboard-art" width="1120" height="504" viewBox="0 0 1120 504">
      <defs>
        <linearGradient id="hazeGradient" x1="0" y1="0" x2="0" y2="1">
          <stop offset="0" stop-color="var(--haze-light)" stop-opacity="0"/>
          <stop offset="0.45" stop-color="var(--haze-teal)" stop-opacity="0.8"/>
          <stop offset="1" stop-color="var(--haze-teal)"/>
        </linearGradient>
        <linearGradient id="cabinGradient" x1="0" y1="0" x2="1" y2="1">
          <stop offset="0" stop-color="var(--cabin-light)"/>
          <stop offset="1" stop-color="var(--cabin-dark)"/>
        </linearGradient>
      </defs>
      <rect x="0" y="240" width="800" height="264" fill="url(#hazeGradient)" role="img" aria-label="Aerial view of a coastal city seen from a helicopter"/>
      <rect x="780" y="0" width="340" height="504" fill="url(#cabinGradient)" role="img" aria-label="Passenger with headset looking out of an open helicopter door"/>
      <path d="M0,470 Q530,280 1120,445 L1120,504 L0,504 Z" fill="var(--brand-blue)" fill-opacity="0.94" stroke="var(--white)" stroke-width="7"/>
    </svg>

    <div class="brand"><span class="brand-dot"></span>kelMARINDO</div>

    <div class="slogan">
      <div class="slogan-top">THE ULTIMATE HELICOPTER</div>
      <div class="slogan-bottom">
        <span class="slogan-doors">DOORS-OFF</span>
        <span class="slogan-experience">EXPERIENCE</span>
      </div>
    </div>

    <div class="tagline">SAY <strong>YES</strong> TO NEW&nbsp; <strong>ADVENTURES</strong></div>

    <div class="price-badge">
      <span class="price-label">Prices<br>Starting at</span>
      <span class="price-amount">$99</span>
    </div>

    <div class="hotline">
      <span class="hotline-label">Hotline: (844) KEL-MARI(ndo)</span>
      <span class="hotline-number">(844) 535-6274</span>
    </div>

    <div class="locations">SARASOTA | TAMPA | NAPLES</div>
    <div class="website">www.kelMARINDO.com</div>
  </div>
</body>
</html>
```